Maple Burrow Canine Massage Needs a Business Card Design

Maple Burrow Canine Massage is a new therapeutic canine massage company located in Nederland, Colorado. I need a business card design that include my logo and basic contact information.

Target Market(s)

Pet owners, veterinarians

Industry/Entity Type

Business

Contact Information for Business Card

Tessa Lindqvist, CCMT
303.581.7296
tessa@mapleburrowmassage.example
www.mapleburrowmassage.example

Colors
6c459b
886aae
b8a6cd
a64599
b768aa
d3a5cc
fbed22

Requirements
Must have
• Font should be similar to font in logo.

```html
<!DOCTYPE html>
<html lang="en">
<head>
<meta charset="utf-8">
<title>Maple Burrow Canine Massage – Business Card</title>
<link href="https://fonts.googleapis.com/css2?family=Quicksand:wght@500;700&display=swap" rel="stylesheet">
<style>
  :root {
    --violet-deep: #6c459b;
    --violet-mid: #886aae;
    --lavender: #b8a6cd;
    --magenta: #a64599;
    --magenta-soft: #b768aa;
    --yellow: #f5d750;
    --yellow-line: #f3e3a0;
    --ink: #1e1e1e;
    --card: #ffffff;
    --backdrop: #ebe6e1;
  }
  * { margin: 0; padding: 0; box-sizing: border-box; }
  html, body {
    width: 1200px; height: 902px; overflow: hidden;
    background: var(--backdrop);
    font-family: "Quicksand", sans-serif;
  }
  .card {
    position: absolute; left: 120px; top: 170px;
    width: 960px; height: 561px;
    background: var(--card);
    box-shadow: 0 6px 24px rgba(0,0,0,.12);
    overflow: hidden;
  }
  .brand {
    position: absolute; left: 40px; top: 130px; width: 300px;
    display: flex; flex-direction: column; align-items: center;
  }
  .brand-dot {
    width: 92px; height: 92px; border-radius: 50%;
    background: var(--lavender);
    margin-bottom: 22px;
  }
  .brand-name {
    color: var(--violet-deep); font-weight: 700; font-size: 27px;
    line-height: 1.2; text-align: center;
  }
  .divider {
    position: absolute; left: 366px; top: 128px;
    width: 1px; height: 295px; background: var(--yellow-line);
  }
  .holder-name {
    position: absolute; left: 420px; top: 134px;
    color: var(--magenta); font-weight: 700; font-size: 32px;
    letter-spacing: .3px; white-space: nowrap;
  }
  .contact {
    position: absolute; left: 422px; top: 304px; right: 28px;
    list-style: none;
  }
  .contact-row {
    display: flex; align-items: center; gap: 10px;
    height: 34px; font-size: 23px; font-weight: 500; color: var(--ink);
    white-space: nowrap;
  }
  .contact-icon { width: 27px; height: 27px; flex: none; }
  .website {
    margin-top: 6px; height: 38px; display: flex; align-items: center;
    color: var(--magenta); font-weight: 700; font-size: 22px; letter-spacing: .8px;
    white-space: nowrap;
  }
  .bands { position: absolute; left: 0; bottom: 0; width: 960px; height: 25px; }
</style>
</head>
<body>
  <main class="card">
    <section class="brand">
      <div class="brand-dot"></div>
      <p class="brand-name">Maple Burrow<br>Canine Massage</p>
    </section>

    <div class="divider"></div>

    <h1 class="holder-name">Tessa Lindqvist, CCMT</h1>

    <ul class="contact">
      <li class="contact-row">
        <svg class="contact-icon" viewBox="0 0 29 29" aria-hidden="true">
          <rect width="29" height="29" fill="var(--yellow)"/>
          <path d="M10 7c1-.6 2-.4 2.5.6l1.2 2.6c.3.8 0 1.5-.7 2l-1 .6c.8 2 2.1 3.6 4 4.6l.8-.9c.6-.6 1.4-.7 2.1-.3l2.4 1.5c.9.6 1 1.6.3 2.4l-1.1 1.2c-1 1-2.7 1.2-4.3.4C12 20 9 16.4 8.3 12.4c-.3-1.7.3-3.3 1.7-4.6z" fill="var(--magenta)"/>
        </svg>
        <span>303.581.7296</span>
      </li>
      <li class="contact-row">
        <svg class="contact-icon" viewBox="0 0 29 29" aria-hidden="true">
          <rect width="29" height="29" fill="var(--yellow)"/>
          <rect x="6" y="9" width="17" height="12" fill="var(--magenta-soft)"/>
          <path d="M6 9l8.5 7L23 9" fill="none" stroke="var(--yellow)" stroke-width="1.5"/>
        </svg>
        <span>tessa@mapleburrowmassage.example</span>
      </li>
      <li class="website">www.mapleburrowmassage.example</li>
    </ul>

    <svg class="bands" viewBox="0 0 960 25" aria-hidden="true">
      <polygon points="0,0 596,0 587,25 0,25" fill="var(--yellow)"/>
      <polygon points="606,0 960,0 960,25 597,25" fill="var(--magenta)"/>
    </svg>
  </main>
</body>
</html>
```